Query A Legal Mentor

We need banner ad design for a new company that supplies supplemental study materials for law students. All content on the site is completely free and we assist law students with supplemental materials for daily course work and for preparing for final exams. The site provides free: Q&A - all answers provided by law professors, Audio Lectures on the most important law school topics, Outline Overviews, Charts and Notes of difficult and confusing law school topics, mini essays with answers for exam preparation.
Updates

ads need to be in the following sizes: 728x90, 160x600, 300x250, 468x60, 120x240

Reason: the ad target market are 'professional students' so it cannot look childish in design. The design must be professional looking.

Target Market(s)

Law Students .. review the QueryALegalMentor.example site

Industry/Entity Type

School

Requirements
Must have
• The word 'Free' must be very prominent throughout the ads
Nice to have
• Try to include 'all of the free items' that are included that the user receives once the register for free for the site. Also the ads may include animation so that each free item the user receives may be able to stand out better.

```html
<!DOCTYPE html>
<html lang="en">
<head>
<meta charset="utf-8">
<title>Query A Legal Mentor – Banner Set</title>
<link rel="stylesheet" href="https://fonts.googleapis.com/css2?family=Roboto:wght@400;500&family=Ubuntu:wght@500;700&display=swap">
<style>
  :root {
    --page-bg: #ececec;
    --page-bg-light: #f6f6f6;
    --header-dark: #4a4a4a;
    --header-darker: #3a3a3a;
    --panel-light: #f1f1f1;
    --panel-mid: #d9d9d9;
    --ink: #1d1d1d;
    --rule: #a9a9a9;
    --blue-top: #1aa3e3;
    --blue-bottom: #0b78bd;
    --green-top: #6ccf45;
    --green-bottom: #2c8d1c;
    --green-edge: #23761a;
    --white: #ffffff;
    --photo-top: #cfd2cf;
    --photo-mid: #4f5a55;
    --photo-bottom: #2c3431;
    --scale: 1.2109;
  }
  * { box-sizing: border-box; margin: 0; padding: 0; }
  html, body {
    width: 1200px; height: 804px; overflow: hidden;
    background: radial-gradient(ellipse at 40% 30%, var(--page-bg-light), var(--page-bg));
    font-family: "Roboto", Arial, sans-serif;
    color: var(--ink);
  }
  .stage {
    position: relative; width: 991px; height: 664px;
    transform: scale(var(--scale)); transform-origin: 0 0;
  }
  .ad {
    position: absolute; overflow: hidden;
    background: linear-gradient(180deg, var(--panel-light), var(--panel-mid));
    box-shadow: 0 0 2px rgba(0,0,0,.18);
  }
  .brand {
    color: var(--white); font-family: "Roboto", Arial, sans-serif; font-weight: 500;
    text-align: center; line-height: 1.05;
  }
  .header {
    background: linear-gradient(180deg, var(--header-dark), var(--header-darker));
    display: flex; align-items: center; justify-content: center;
  }
  .headline { font-weight: 500; text-align: center; color: var(--ink); }
  .rule { height: 1px; background: var(--rule); margin: 0 auto; }
  .offer-list { list-style: none; text-align: center; color: var(--ink); }
  .cta-band {
    background: linear-gradient(180deg, var(--blue-top), var(--blue-bottom));
    display: flex; align-items: center; justify-content: center;
  }
  .cta {
    display: flex; align-items: stretch; border-radius: 999px;
    background: linear-gradient(180deg, var(--green-top), var(--green-bottom));
    border: 1px solid var(--green-edge);
    box-shadow: 0 2px 3px rgba(0,0,0,.35), inset 0 1px 0 rgba(255,255,255,.35);
    color: var(--white); font-family: "Ubuntu", Arial, sans-serif; font-weight: 700;
    text-shadow: 0 1px 1px rgba(0,0,0,.3);
  }
  .cta-label { flex: 1; display: flex; align-items: center; justify-content: center; white-space: nowrap; }
  .cta-arrow {
    display: flex; align-items: center; justify-content: center;
    border-left: 1px solid rgba(0,0,0,.25);
    box-shadow: inset 1px 0 0 rgba(255,255,255,.25);
  }

  /* 160 x 600 skyscraper */
  .ad-skyscraper { left: 44px; top: 32px; width: 160px; height: 600px; }
  .ad-skyscraper .header { height: 40px; }
  .ad-skyscraper .brand { font-size: 14px; white-space: nowrap; }
  .ad-skyscraper .headline { font-size: 19px; line-height: 25px; margin-top: 14px; }
  .ad-skyscraper .rule { width: 144px; margin-top: 14px; }
  .ad-skyscraper .offer-list { font-size: 16px; line-height: 19px; margin-top: 10px; }
  .ad-skyscraper .offer-list li { margin-bottom: 4px; }
  .photo-area {
    position: absolute; left: 36px; top: 312px; width: 92px; height: 212px;
    background: linear-gradient(180deg, var(--photo-top) 0%, var(--photo-mid) 25%, var(--photo-bottom) 100%);
    border-radius: 40px 40px 4px 4px; opacity: .85;
  }
  .ad-skyscraper .cta-band { position: absolute; left: 0; bottom: 0; width: 160px; height: 75px; }
  .ad-skyscraper .cta { width: 145px; height: 30px; font-size: 15px; }
  .ad-skyscraper .cta-arrow { width: 24px; }

  /* 728 x 90 leaderboard */
  .ad-leaderboard { left: 219px; top: 32px; width: 728px; height: 90px; }
  .ad-leaderboard .brand-block { position: absolute; left: 0; top: 0; width: 150px; height: 90px; }
  .ad-leaderboard .brand { position: absolute; left: 10px; top: 0; width: 122px; height: 90px; display: flex; align-items: center; justify-content: center; font-size: 17px; }
  .ad-leaderboard .copy { position: absolute; left: 150px; top: 0; width: 399px; text-align: center; }
  .ad-leaderboard .headline { font-size: 18px; line-height: 20px; margin-top: 4px; }
  .ad-leaderboard .rule { width: 300px; margin-top: 4px; }
  .ad-leaderboard .offer-list { font-size: 13px; line-height: 16px; margin-top: 3px; }
  .ad-leaderboard .cta-band { position: absolute; right: 0; top: 0; width: 179px; height: 90px; }
  .ad-leaderboard .cta { width: 156px; height: 32px; font-size: 15px; }
  .ad-leaderboard .cta-arrow { width: 22px; }

  /* 468 x 60 banner */
  .ad-banner { left: 219px; top: 137px; width: 468px; height: 60px; }
  .ad-banner .brand-block { position: absolute; left: 0; top: 0; width: 96px; height: 60px; }
  .ad-banner .brand { position: absolute; left: 4px; top: 0; width: 80px; height: 60px; display: flex; align-items: center; justify-content: center; font-size: 11px; }
  .ad-banner .copy { position: absolute; left: 96px; top: 0; width: 257px; height: 60px; display: flex; align-items: center; justify-content: center; }
  .ad-banner .headline { font-size: 14.5px; line-height: 18px; }
  .ad-banner .cta-band { position: absolute; right: 0; top: 0; width: 115px; height: 60px; }
  .ad-banner .cta { width: 96px; height: 22px; font-size: 10px; }
  .ad-banner .cta-arrow { width: 14px; }

  /* 300 x 250 rectangle */
  .ad-rectangle { left: 219px; top: 212px; width: 300px; height: 250px; }
  .ad-rectangle .header { height: 36px; }
  .ad-rectangle .brand { font-size: 17px; }
  .ad-rectangle .headline { font-size: 18.5px; line-height: 24.5px; margin-top: 10px; }
  .ad-rectangle .rule { width: 236px; margin-top: 9px; }
  .ad-rectangle .offer-list { font-size: 13px; line-height: 16px; margin-top: 5px; }
  .ad-rectangle .cta-band { position: absolute; left: 0; bottom: 0; width: 300px; height: 52px; }
  .ad-rectangle .cta { width: 156px; height: 32px; font-size: 15px; }
  .ad-rectangle .cta-arrow { width: 22px; }

  /* 120 x 240 vertical */
  .ad-vertical { left: 534px; top: 212px; width: 120px; height: 240px; }
  .ad-vertical .header { height: 38px; padding: 0 3px; }
  .ad-vertical .brand { font-size: 10.5px; white-space: nowrap; }
  .ad-vertical .headline { font-size: 12.5px; line-height: 16.5px; margin-top: 5px; }
  .ad-vertical .rule { width: 106px; margin-top: 5px; }
  .ad-vertical .offer-list { font-size: 11px; line-height: 13px; margin-top: 3px; }
  .ad-vertical .cta-band { position: absolute; left: 0; bottom: 0; width: 120px; height: 34px; }
  .ad-vertical .cta { width: 108px; height: 23px; font-size: 10.5px; }
  .ad-vertical .cta-arrow { width: 16px; }
</style>
</head>
<body>
<main class="stage">

  <section class="ad ad-skyscraper" aria-label="160 by 600 skyscraper ad">
    <header class="header"><span class="brand">Query A Legal Mentor</span></header>
    <h2 class="headline">Your Personal<br>Tutor &amp; Everything<br>Resource for<br>Legal Education.</h2>
    <div class="rule"></div>
    <ul class="offer-list">
      <li>Q &amp; A</li>
      <li>Topic Videos/<br>Audio lectures</li>
      <li>Outline Overviews</li>
      <li>Charts and Notes</li>
      <li>Mini Essays</li>
    </ul>
    <div class="photo-area" role="img" aria-label="Photo area for a dark bronze sculpture"></div>
    <div class="cta-band">
      <a class="cta"><span class="cta-label">Get it for FREE</span><span class="cta-arrow"><svg width="8" height="10" viewBox="0 0 8 10"><polyline points="2,1 6,5 2,9" fill="none" stroke="#fff" stroke-width="2"/></svg></span></a>
    </div>
  </section>

  <section class="ad ad-leaderboard" aria-label="728 by 90 leaderboard ad">
    <svg class="brand-block" viewBox="0 0 150 90" preserveAspectRatio="none"><polygon points="0,0 130,0 146,45 130,90 0,90" fill="#474747"/></svg>
    <span class="brand">Query A Legal Mentor</span>
    <div class="copy">
      <h2 class="headline">Your Personal Tutor &amp; Everything<br>Resource for Legal Education.</h2>
      <div class="rule"></div>
      <p class="offer-list">Q &amp; A - Topic Videos/Audio lectures - Outline Overviews -<br>Charts and Notes - Mini Essays</p>
    </div>
    <div class="cta-band">
      <a class="cta"><span class="cta-label">Get it for FREE</span><span class="cta-arrow"><svg width="8" height="10" viewBox="0 0 8 10"><polyline points="2,1 6,5 2,9" fill="none" stroke="#fff" stroke-width="2"/></svg></span></a>
    </div>
  </section>

  <section class="ad ad-banner" aria-label="468 by 60 banner ad">
    <svg class="brand-block" viewBox="0 0 96 60" preserveAspectRatio="none"><polygon points="0,0 84,0 94,30 84,60 0,60" fill="#474747"/></svg>
    <span class="brand">Query A Legal Mentor</span>
    <div class="copy">
      <h2 class="headline">Your Personal Tutor &amp; Everything<br>Resource for Legal Education.</h2>
    </div>
    <div class="cta-band">
      <a class="cta"><span class="cta-label">Get it for FREE</span><span class="cta-arrow"><svg width="6" height="8" viewBox="0 0 8 10"><polyline points="2,1 6,5 2,9" fill="none" stroke="#fff" stroke-width="2"/></svg></span></a>
    </div>
  </section>

  <section class="ad ad-rectangle" aria-label="300 by 250 rectangle ad">
    <header class="header"><span class="brand">Query A Legal Mentor</span></header>
    <h2 class="headline">Your Personal Tutor<br>&amp; Everything Resource<br>for Legal Education.</h2>
    <div class="rule"></div>
    <p class="offer-list">Q &amp; A - Topic Videos/Audio lectures -<br>Outline Overviews - Charts and Notes -<br>Mini Essays</p>
    <div class="cta-band">
      <a class="cta"><span class="cta-label">Get it for FREE</span><span class="cta-arrow"><svg width="8" height="10" viewBox="0 0 8 10"><polyline points="2,1 6,5 2,9" fill="none" stroke="#fff" stroke-width="2"/></svg></span></a>
    </div>
  </section>

  <section class="ad ad-vertical" aria-label="120 by 240 vertical ad">
    <header class="header"><span class="brand">Query A Legal Mentor</span></header>
    <h2 class="headline">Your Personal<br>Tutor &amp; Everything<br>Resource for<br>Legal Education.</h2>
    <div class="rule"></div>
    <p class="offer-list">Q &amp; A -<br>Topic Videos/<br>Audio lectures -<br>Outline Overviews -<br>Charts and Notes -<br>Mini Essays</p>
    <div class="cta-band">
      <a class="cta"><span class="cta-label">Get it for FREE</span><span class="cta-arrow"><svg width="6" height="8" viewBox="0 0 8 10"><polyline points="2,1 6,5 2,9" fill="none" stroke="#fff" stroke-width="2"/></svg></span></a>
    </div>
  </section>

</main>
</body>
</html>
```